Refresh of The Marwick Partners business card

Update business card design using existing primary logo. Names, numbers, etc. are too hard to read on current design.

Target Market(s)

We are a CPA firm.

Industry/Entity Type

Accountant

Contact Information for Business Card

update current card

Colors
0355a3
3176b5
85acd3
0792cd

Requirements
Must have
• Easier to read phone numbers and names
• Use existing logo
Nice to have
• We love our color scheme and current TMP logo. But the names and phone numbers are too small and card just look old and stale.

```html
<!DOCTYPE html>
<html lang="en">
<head>
<meta charset="utf-8">
<title>The Marwick Partners — Business Card</title>
<link rel="stylesheet" href="https://fonts.googleapis.com/css2?family=Cinzel:wght@700&family=Roboto:wght@400;500&display=swap">
<style>
  :root {
    --backdrop: #2a2a2c;
    --card: #f3f3f3;
    --brand-blue: #0355a3;
    --brand-deep: #0a3f86;
    --brand-mid: #3176b5;
    --ring-grey: #555555;
    --text-grey: #555a60;
  }
  * { margin: 0; padding: 0; box-sizing: border-box; }
  html, body { width: 1200px; height: 960px; overflow: hidden; background: var(--backdrop); }
  .stage { position: relative; width: 1200px; height: 960px; }

  .card {
    position: absolute;
    width: 600px;
    height: 342px;
    background: var(--card);
    border-radius: 16px;
    overflow: hidden;
  }
  .card--front { left: 305px; top: 133px; }
  .card--back  { left: 301px; top: 492px; }

  .brand-band {
    position: absolute; left: 0; top: 38px; width: 44px; height: 84px;
    background: linear-gradient(180deg, var(--brand-mid), var(--brand-deep));
  }
  .brand-dot {
    position: absolute; left: 38px; top: 38px; width: 84px; height: 84px;
    border-radius: 50%;
    background: var(--brand-blue);
    border: 3px solid var(--card);
    box-shadow: 0 0 0 2px var(--ring-grey);
  }
  .wordmark {
    position: absolute;
    font-family: "Cinzel", Georgia, serif;
    font-weight: 700;
    color: var(--brand-blue);
    line-height: 1.05;
    letter-spacing: 0.02em;
    white-space: nowrap;
  }
  .card--front .wordmark { left: 136px; top: 50px; font-size: 19px; }
  .tagline {
    position: absolute;
    font-family: "Roboto", Arial, sans-serif;
    font-size: 7px;
    letter-spacing: 0.2em;
    color: var(--text-grey);
    text-transform: uppercase;
    white-space: nowrap;
  }
  .card--front .tagline { left: 136px; top: 110px; }

  .address {
    position: absolute; left: 38px; top: 172px;
    font-family: "Roboto", Arial, sans-serif;
    font-size: 16px; line-height: 21px;
    font-style: normal;
    color: var(--text-grey);
  }
  .contact-list {
    position: absolute; left: 40px; top: 226px;
    list-style: none;
    font-family: "Roboto", Arial, sans-serif;
    font-size: 16px; line-height: 20.5px;
    color: var(--text-grey);
  }
  .contact-list li { display: flex; align-items: center; gap: 9px; }
  .contact-list svg { width: 14px; height: 14px; fill: var(--brand-deep); flex: none; }

  .holder-name {
    position: absolute; right: 44px; top: 252px;
    font-family: "Cinzel", Georgia, serif;
    font-weight: 700; font-size: 18px;
    color: var(--brand-blue);
    letter-spacing: 0.02em;
    white-space: nowrap;
  }

  .card--back .wordmark { left: 34px; top: 214px; font-size: 25px; }
  .card--back .tagline { left: 34px; top: 287px; font-size: 8px; }
  .website {
    position: absolute; left: 34px; top: 299px;
    font-family: "Roboto", Arial, sans-serif;
    font-size: 16px; color: var(--text-grey); letter-spacing: 0.03em;
  }
  .emblem-disc {
    position: absolute; left: 266px; top: 10px; width: 308px; height: 322px;
    border-radius: 50%;
    background: radial-gradient(circle at 40% 35%, var(--brand-mid), var(--brand-blue) 60%, var(--brand-deep));
    border: 9px solid var(--ring-grey);
    box-shadow: inset 0 0 0 4px var(--card);
  }
</style>
</head>
<body>
<main class="stage">

  <section class="card card--front" aria-label="Card front">
    <div class="brand-band"></div>
    <div class="brand-dot"></div>
    <div class="wordmark">THE MARWICK<br>PARTNERS</div>
    <div class="tagline">Certified Public Accountants</div>

    <address class="address">
      318 Lakeview Ave. Suite 104<br>
      Winter Park, Florida 32789
    </address>

    <ul class="contact-list">
      <li>
        <svg viewBox="0 0 24 24" aria-hidden="true"><path d="M6.6 10.8a15.1 15.1 0 0 0 6.6 6.6l2.2-2.2a1 1 0 0 1 1-.25 11.4 11.4 0 0 0 3.6.57 1 1 0 0 1 1 1V20a1 1 0 0 1-1 1A17 17 0 0 1 3 4a1 1 0 0 1 1-1h3.5a1 1 0 0 1 1 1c0 1.250.2 2.45.57 3.57a1 1 0 0 1-.25 1z"/></svg>
        407.555.0142
      </li>
      <li>
        <svg viewBox="0 0 24 24" aria-hidden="true"><path d="M7 1h10a2 2 0 0 1 2 2v18a2 2 0 0 1-2 2H7a2 2 0 0 1-2-2V3a2 2 0 0 1 2-2zm0 3v14h10V4zm5 15.5a1 1 0 1 0 0 2 1 1 0 0 0 0-2z"/></svg>
        407.555.0187
      </li>
      <li>
        <svg viewBox="0 0 24 24" aria-hidden="true"><path d="M6 2h12v6H6zM3 9h18a1 1 0 0 1 1 1v8h-4v4H6v-4H2v-8a1 1 0 0 1 1-1zm5 7v4h8v-4z"/></svg>
        407.555.0163
      </li>
      <li>
        <svg viewBox="0 0 24 24" aria-hidden="true"><path d="M2 5h20v14H2zm2 2v.5l8 5 8-5V7zm0 2.9V17h16V9.9l-8 5z"/></svg>
        dan@marwickpartners.com
      </li>
    </ul>

    <div class="holder-name">DANIEL R. MARWICK, CPA</div>
  </section>

  <section class="card card--back" aria-label="Card back">
    <div class="wordmark">THE MARWICK<br>PARTNERS</div>
    <div class="tagline">Certified Public Accountants</div>
    <div class="website">www.marwickpartners.com</div>
    <div class="emblem-disc"></div>
  </section>

</main>
</body>
</html>
```